Pest Control Company needs business card!

Hi there, we need a business card designed for our new Pest Control Company. Ideally this card will be simple, yet feel elegant and high end. We want to use the colours Orange, Black and White. Please see our attached logo for the exact colours.

Business card details:

Phone - 0461 275 804
Name - Gavin Holloway
Email - Info@steadfastverminguard.com.au

We would also like to include the following list with dot points:

SERVICES / INSPECTIONS

Termites, Wood Borers, Ants, Cockroaches, Spiders, Fleas, Mice, Rats, Bed Bugs, & More!

```html
<!DOCTYPE html>
<html lang="en">
<head>
<meta charset="utf-8">
<title>Steadfast Vermin Guard – Business Card</title>
<link rel="stylesheet" href="https://fonts.googleapis.com/css2?family=Josefin+Sans:wght@400;700&display=swap">
<style>
  :root {
    --backdrop: #e4e4e4;
    --paper: #f7f7f5;
    --ink: #1c1c1c;
    --accent: #d3262b;
    --emboss: #2e2e2e;
    --light-text: #f0f0f0;
  }
  * { box-sizing: border-box; margin: 0; padding: 0; }
  html, body { width: 1200px; height: 801px; overflow: hidden; }
  body {
    background: var(--backdrop);
    font-family: "Josefin Sans", sans-serif;
    display: flex;
    align-items: center;
    justify-content: center;
    gap: 48px;
  }
  .card {
    position: relative;
    width: 520px;
    height: 318px;
    overflow: hidden;
    box-shadow: 0 6px 18px rgba(0,0,0,0.18);
  }
  .card--front { background: var(--paper); }
  .card--back { background: var(--ink); display: flex; align-items: center; justify-content: center; }

  .front-shapes { position: absolute; inset: 0; }

  .brand {
    position: absolute;
    display: flex;
    align-items: center;
    gap: 10px;
    font-weight: 700;
    text-transform: uppercase;
    line-height: 1;
  }
  .brand__mark { border-radius: 50%; flex: none; }
  .brand__name span { display: block; }

  .card--front .brand { left: 30px; top: 38px; color: var(--ink); }
  .card--front .brand__mark { width: 18px; height: 18px; background: var(--ink); }
  .card--front .brand__name { font-size: 24px; letter-spacing: 0.5px; }

  .card--back .brand { position: static; color: var(--emboss); }
  .card--back .brand__mark { width: 28px; height: 28px; background: var(--emboss); }
  .card--back .brand__name { font-size: 38px; letter-spacing: 1px; }

  .services {
    position: absolute;
    right: 24px;
    top: 26px;
    width: 250px;
    text-align: right;
    color: var(--ink);
  }
  .services__title {
    color: var(--accent);
    font-size: 15px;
    font-weight: 400;
    letter-spacing: 0.5px;
    margin-bottom: 6px;
  }
  .services__list { font-size: 12.5px; line-height: 1.45; }

  .contact {
    position: absolute;
    left: 30px;
    bottom: 22px;
    color: var(--light-text);
  }
  .contact__name {
    color: var(--accent);
    font-size: 19px;
    font-weight: 400;
    letter-spacing: 0.5px;
    margin-bottom: 10px;
  }
  .contact__line {
    display: flex;
    align-items: center;
    gap: 8px;
    font-size: 12.5px;
    margin-top: 4px;
  }
  .contact__icon { width: 12px; height: 12px; flex: none; }
</style>
</head>
<body>

  <section class="card card--front">
    <svg class="front-shapes" viewBox="0 0 520 318" aria-hidden="true">
      <polygon points="410,95 520,95 520,160 380,175" fill="var(--accent)"/>
      <polygon points="0,212 300,212 380,175 520,160 520,318 0,318" fill="var(--ink)"/>
    </svg>

    <div class="brand">
      <span class="brand__mark"></span>
      <div class="brand__name"><span>Steadfast</span><span>Vermin</span><span>Guard</span></div>
    </div>

    <div class="services">
      <h2 class="services__title">SERVICES / INSPECTIONS</h2>
      <p class="services__list">Termites, Wood Borers, Ants<br>Cockroaches, Spiders, Fleas<br>Mice, Rats, Bed Bugs, &amp; More!</p>
    </div>

    <div class="contact">
      <h1 class="contact__name">GAVIN HOLLOWAY</h1>
      <p class="contact__line">
        <svg class="contact__icon" viewBox="0 0 12 12" aria-hidden="true">
          <circle cx="6" cy="6" r="6" fill="var(--accent)"/>
          <path d="M4 3.2 L5 3 L5.6 4.6 L5 5.1 Q5.6 6.5 6.9 7 L7.4 6.4 L9 7 L8.8 8 Q6.8 8.6 5 6.8 Q3.4 5 4 3.2Z" fill="var(--ink)"/>
        </svg>
        0461 275 804
      </p>
      <p class="contact__line">
        <svg class="contact__icon" viewBox="0 0 12 12" aria-hidden="true">
          <circle cx="6" cy="6" r="6" fill="var(--accent)"/>
          <rect x="3" y="4" width="6" height="4.2" fill="none" stroke="var(--ink)" stroke-width="0.9"/>
          <path d="M3 4 L6 6.3 L9 4" fill="none" stroke="var(--ink)" stroke-width="0.9"/>
        </svg>
        Info@steadfastverminguard.com.au
      </p>
    </div>
  </section>

  <section class="card card--back">
    <div class="brand">
      <span class="brand__mark"></span>
      <div class="brand__name"><span>Steadfast</span><span>Vermin Guard</span></div>
    </div>
  </section>

</body>
</html>
```